New IT company website using Wordpress

Our current website (www.quendrix.co.uk) is getting rather dated and looks too home-made! We require a new, fresher look and feel using a platform that lets us easily change the content without having to edit the html pages. Wordpress seems to be the ticket for that.
We are a technology consultancy and sell, install and support smart-print and document workflow software solutions. Smart-Print software (Tolvane) helps companies to control print oputput, reduce wasteage and cost. Workflow is all about scanning and digitising paper documents and then routing them to other business systems.
We'd like some kind of banner section that loops through 3-4 images with some text on them - each representing a key area of expertiese or product.
The idea is that we get a template that all pages fit into. Ideally with slighly different colour schemes for each of the areas of business.
We have a logo on the current website that is still up-to-date.
We have 3-4 key areas of interest and the new design should accomodate that somehow. I upload a document to show the stucture of the new site for info only.
Printer and copier resellers; some end-users, particular in higher education
Software

```html
<!DOCTYPE html>
<html lang="en">
<head>
<meta charset="utf-8">
<title>Quendrix Solutions</title>
<link href="https://fonts.googleapis.com/css2?family=Open+Sans:wght@400;600;700&display=swap" rel="stylesheet">
<style>
:root{
  --teal:#1f8a78;
  --teal-dark:#16665a;
  --teal-deep:#0f4f47;
  --orange:#f39a1f;
  --page:#ececec;
  --white:#ffffff;
  --text:#555555;
  --footer:#2b2b2b;
  --footer-line:#f2c200;
}
*{box-sizing:border-box;margin:0;padding:0}
html,body{width:744px;height:1200px;overflow:hidden}
body{position:relative;background:var(--page);font-family:"Open Sans",Arial,sans-serif;color:var(--text);font-size:8px;line-height:1.45}
.abs{position:absolute}
.site-header{left:0;top:0;width:744px;height:108px;display:flex;flex-direction:column;align-items:center;justify-content:center;gap:4px}
.brand-mark{width:34px;height:34px;background:var(--teal)}
.brand-name{font-size:11px;font-weight:600;color:var(--teal-dark);letter-spacing:.5px}
.main-nav{left:70px;top:108px;width:604px;height:26px;background:var(--teal);display:flex;align-items:center}
.main-nav a{color:var(--white);text-decoration:none;font-size:9px;padding:0 14px;height:26px;line-height:26px}
.main-nav a.active{background:var(--teal-deep)}
.main-nav .nav-mail{margin-left:auto;font-size:8px}
.hero-image{left:70px;top:134px;width:410px;height:238px;background:linear-gradient(135deg,#e8ebe6 0%,#c9cfc6 45%,#8e9990 100%)}
.hero-caption{left:170px;top:200px;width:220px;background:rgba(31,138,120,.92);color:var(--white);padding:8px 10px}
.hero-caption h1{font-size:11px;line-height:1.3;font-weight:600}
.hero-caption p{font-size:7px;margin-top:4px;opacity:.9}
.slider-dots{left:255px;top:358px;display:flex;gap:4px}
.slider-dots span{width:6px;height:6px;border-radius:50%;background:var(--white);opacity:.6}
.slider-dots span.on{opacity:1;background:var(--teal)}
.trial-panel{left:480px;top:134px;width:194px;height:238px;background:var(--teal);padding:12px 14px;color:var(--white)}
.trial-panel h2{font-size:11px;font-weight:700;text-align:center}
.trial-panel .sub{font-size:7px;text-align:center;margin-bottom:8px}
.field{background:var(--white);height:22px;margin-bottom:8px;display:flex;align-items:center;padding-left:8px;color:#999;font-size:8px}
.field i{width:8px;height:8px;background:var(--teal);margin-right:6px;display:block}
.btn-submit{background:var(--orange);color:var(--white);font-weight:700;font-size:10px;text-align:center;height:24px;line-height:24px}
.card{top:405px;width:190px;height:205px;background:var(--white)}
.card .pic{height:78px}
.card h3{height:18px;line-height:18px;background:var(--teal);color:var(--white);font-size:9px;font-weight:600;text-align:center}
.card p{padding:6px 8px;font-size:7px;height:82px}
.card .more{position:absolute;right:8px;bottom:10px;background:var(--teal-dark);color:var(--white);font-size:7px;padding:2px 7px}
.components{left:70px;top:622px;width:604px;height:236px;background:var(--teal-dark)}
.chart-box{left:14px;top:14px;width:180px;height:140px;background:var(--white);padding:6px}
.chart-box .t{font-size:7px;font-weight:700;color:#333}
.chart-box .s{font-size:6px;color:#777}
.comp-text{left:210px;top:14px;width:220px;color:var(--white)}
.comp-text h2{font-size:11px;font-weight:600;margin-bottom:6px}
.comp-text p{font-size:7px;opacity:.9}
.btn-read{display:inline-block;margin-top:10px;background:var(--orange);color:var(--white);font-size:8px;font-weight:600;padding:3px 12px}
.testimonials{left:446px;top:10px;width:146px;height:212px;background:var(--teal-deep);padding:8px;color:var(--white)}
.testimonials h3{font-size:10px;font-weight:600;margin-bottom:6px}
.quote{background:var(--teal);padding:8px;font-size:7px;font-style:normal}
.quote-by{text-align:right;margin-top:6px;font-size:7px}
.services{left:70px;top:866px;width:604px;height:234px;background:var(--white);padding:18px 22px}
.services h2{font-size:12px;font-weight:600;color:#333;margin-bottom:8px}
.services p{width:300px;font-size:7px}
.service-list{width:300px;display:grid;grid-template-columns:1fr 1fr;gap:5px 12px;margin-top:12px;list-style:none}
.service-list li{font-size:7px;display:flex;align-items:center;gap:4px}
.service-list li::before{content:"";width:6px;height:6px;background:var(--teal);display:block}
.services-pic{left:340px;top:70px;width:240px;height:120px;background:linear-gradient(135deg,#dfe7ef,#9db3c8)}
.site-footer{left:0;top:1104px;width:744px;height:96px;background:var(--footer);border-top:3px solid var(--footer-line);color:#ccc}
.site-footer h4{color:var(--white);font-size:10px;font-weight:600;margin-bottom:4px}
.foot-company{left:70px;top:8px}
.foot-company li{list-style:none;font-size:7px;line-height:1.45}
.foot-news{left:170px;top:8px;width:170px}
.news-date{float:left;width:26px;height:28px;background:var(--teal);color:var(--white);text-align:center;font-size:6px;margin-right:6px;padding-top:2px}
.news-date b{display:block;font-size:12px;line-height:1}
.foot-news p{font-size:7px}
.foot-contact{left:350px;top:8px;width:110px}
.foot-contact .f{height:13px;background:#444;margin-bottom:4px;font-size:6px;padding-left:4px;line-height:13px;color:#999}
.foot-contact .send{width:50px;height:14px;background:var(--teal);color:var(--white);font-size:7px;text-align:center;line-height:14px}
.foot-info{left:475px;top:8px;width:200px;font-size:7px}
.foot-info .phone{font-size:10px;color:var(--white);font-weight:600}
.socials{display:flex;gap:3px;margin-top:4px}
.socials span{width:11px;height:11px;background:#555;display:block}
</style>
</head>
<body>
<header class="site-header abs">
  <div class="brand-mark"></div>
  <div class="brand-name">Quendrix Solutions</div>
</header>

<nav class="main-nav abs">
  <a class="active">Home</a><a>Smart Print</a><a>Reporting</a><a>Workflow</a><a>Services</a><a>Support</a><a>About</a>
  <a class="nav-mail">support@quendrix.co.uk</a>
</nav>

<div class="hero-image abs" role="img" aria-label="Office with a multifunction printer and copier"></div>
<div class="hero-caption abs">
  <h1>Smart Secure Document Accounting, Flow and Reporting Solutions</h1>
  <p>Control print output, reduce waste and route documents securely across your organisation.</p>
</div>
<div class="slider-dots abs"><span class="on"></span><span></span><span></span><span></span></div>

<aside class="trial-panel abs">
  <h2>DOWNLOAD FREE TRIAL</h2>
  <div class="sub">Fill in your details to get a trial of our software</div>
  <div class="field"><i></i>Name</div>
  <div class="field"><i></i>Organisation</div>
  <div class="field"><i></i>Email Address</div>
  <div class="field"><i></i>Telephone</div>
  <div class="btn-submit">SUBMIT</div>
</aside>

<section class="card abs" style="left:70px">
  <div class="pic" role="img" aria-label="Office printer" style="background:linear-gradient(135deg,#f1f1f1,#bfc6c3)"></div>
  <h3>Smart Print</h3>
  <p>Tolvane Smart Print solutions track every page printed across your fleet, cut waste and lower running costs for office and campus users.</p>
  <span class="more">+ More info</span>
</section>
<section class="card abs" style="left:277px">
  <div class="pic" role="img" aria-label="Colourful 3D bar graph" style="background:linear-gradient(90deg,#f6e3b0,#e8b4c8,#b9d4ee)"></div>
  <h3>Reporting</h3>
  <p>Quendrix reporting tools turn print and scan data into clear monthly reports, so managers can see usage, trends and savings at a glance.</p>
  <span class="more">+ More info</span>
</section>
<section class="card abs" style="left:484px">
  <div class="pic" role="img" aria-label="Interlocking gears" style="background:linear-gradient(135deg,#eef3f2,#9fb6b2)"></div>
  <h3>Workflow</h3>
  <p>Our workflow tools capture paper documents, convert them into searchable files and route them straight into the business systems you already use.</p>
  <span class="more">+ More info</span>
</section>

<section class="components abs">
  <div class="chart-box abs">
    <div class="t">Quendrix Advanced Reporting</div>
    <div class="s">Print and Copy Pages per Month</div>
    <svg width="168" height="106" viewBox="0 0 168 106">
      <line x1="14" y1="96" x2="162" y2="96" stroke="#999" stroke-width="1"/>
      <line x1="14" y1="6" x2="14" y2="96" stroke="#999" stroke-width="1"/>
      <g fill="#4f81bd">
        <rect x="20" y="40" width="12" height="56"/>
        <rect x="38" y="30" width="12" height="66"/>
        <rect x="56" y="50" width="12" height="46"/>
        <rect x="74" y="22" width="12" height="74"/>
      </g>
      <g fill="#c0504d">
        <rect x="92" y="36" width="12" height="60"/>
        <rect x="110" y="18" width="12" height="78"/>
      </g>
      <g fill="#9bbb59">
        <rect x="128" y="44" width="12" height="52"/>
        <rect x="146" y="28" width="12" height="68"/>
      </g>
    </svg>
  </div>
  <div class="comp-text abs">
    <h2>Custom Quendrix software components</h2>
    <p>We build custom software components that connect print, scan and reporting tools to your existing systems. Each module is tested, documented and supported by our own team, so your staff get a solution that fits the way they already work.</p>
    <span class="btn-read">Read More</span>
  </div>
  <div class="testimonials abs">
    <h3>Testimonials</h3>
    <blockquote class="quote">Quendrix made our print rollout painless. Costs dropped in the first term and their support team always answers quickly.</blockquote>
    <div class="quote-by">Eleanor</div>
  </div>
</section>

<section class="services abs">
  <h2>Our Services</h2>
  <p>From first assessment to installation and ongoing support, we help resellers and end users get more from their print and document workflow software.</p>
  <ul class="service-list">
    <li>Managed Print Solutions</li><li>Office Workflow Solutions</li>
    <li>Production Printing</li><li>Professional Services</li>
    <li>Document Scanning</li><li>Custom Software</li>
    <li>Secure Release</li><li>Maintenance &amp; Support</li>
  </ul>
  <div class="services-pic abs" role="img" aria-label="Business charts and papers on a desk"></div>
</section>

<footer class="site-footer abs">
  <div class="foot-company abs">
    <h4>Company</h4>
    <ul><li>Home</li><li>Smart Print</li><li>Reporting</li><li>Workflow</li><li>Services</li><li>Support</li></ul>
  </div>
  <div class="foot-news abs">
    <h4>News</h4>
    <div class="news-date">MAY<b>27</b></div>
    <p>Quendrix joins new campus print programme with three universities this spring.</p>
  </div>
  <div class="foot-contact abs">
    <h4>Contact Us</h4>
    <div class="f">Name</div><div class="f">Email</div><div class="f">Message</div>
    <div class="send">Submit</div>
  </div>
  <div class="foot-info abs">
    <div>42 Harrow Lane<br>Dunmore</div>
    <div class="phone">+44 161 555 0192</div>
    <div class="phone">0161 555 0193</div>
    <div>info@quendrix.co.uk</div>
    <div class="socials"><span></span><span></span><span></span><span></span></div>
  </div>
</footer>
</body>
</html>
```